Mobile Command - Design a new page for our website

The designer is to use our existing website to match color and style and the documents provided to create a webpage that reflects the information in the brochure attached. This should also include a button to download our brochure and a form to request more information by entering name, phone, and email. This page will be added to our main site and will be coded by our webmaster team.

View website at www.harborlinepatrol.us

The successful designer will be asked to also design another page for additional compensation.

Target Market(s)

Security and Law Enforcement

Industry/Entity Type

Security Service

Coding

Coded - Design and coding required

Number of Pages Required

1 page

Font styles to use
Other font styles liked:
• Raleway or match site font and style

Requirements
Must have
• Match in color and style to our existing site as this page will be added to the existing website.

UPDATE: Place QVT Logo (attached to the brief) in a horizontal bar the width of the page with the following text:

"Mobile Command and all of Harborline's services are available on under our QVT Contract." (Add button) Click for Info
Nice to have
• Simple design expressing clean and easy to comprehend points

Please be creative, use the ability to scroll vertically on the page to space out the content and add supporting graphics or images.

```html
<!DOCTYPE html>
<html lang="en">
<head>
<meta charset="utf-8">
<title>Mobile Command – Harborline Consulting</title>
<link href="https://fonts.googleapis.com/css2?family=Raleway:wght@400;500;600;700;800&display=swap" rel="stylesheet">
<style>
:root{
  --brand-blue:#2f6eb5;
  --brand-blue-dark:#285f9e;
  --heading-blue:#3372b9;
  --ink:#333;
  --ink-soft:#555;
  --band:#f2f2f2;
  --white:#fff;
  --alert-red:#e8121b;
  --rule:#b9c9dd;
}
*{box-sizing:border-box;margin:0;padding:0}
html,body{width:834px;height:1200px;overflow:hidden;background:var(--white)}
body{font-family:'Raleway',sans-serif;color:var(--ink);position:relative}
.abs{position:absolute}

/* Header */
.site-header{left:0;top:0;width:834px;height:30px;background:var(--brand-blue)}
.brand{left:161px;top:5px;color:var(--white);font-weight:700;font-size:16px;line-height:18px;display:flex;align-items:center;gap:5px}
.brand-mark{width:10px;height:10px;border-radius:50%;background:var(--white)}
.nav a{position:absolute;top:0;height:30px;line-height:28px;color:var(--white);font-size:7.3px;text-decoration:none}
.nav .active{background:var(--brand-blue-dark);padding:0 7px}
.nav .contact{top:8px;height:11px;line-height:11px;background:var(--alert-red);padding:0 3px;border-radius:1px}

/* Hero */
.hero-photo{left:0;top:30px;width:834px;height:260px;background:linear-gradient(180deg,#3d3a3d 0%,#54423f 45%,#4a3433 75%,#3a2d2f 100%)}
.hero-title{left:161px;top:74px;color:var(--white);font-weight:800;font-size:21.5px;letter-spacing:.2px}
.hero-sub{left:161px;top:100px;color:var(--white);font-size:10.7px;letter-spacing:.2px}
.btn-download{left:161px;top:153px;width:155px;height:32px;background:var(--brand-blue);border-radius:3px;color:var(--white);text-align:center;padding-top:4px}
.btn-download strong{display:block;font-size:12px;font-weight:800;line-height:14px}
.btn-download span{display:block;font-size:6.8px;font-weight:600;line-height:9px}
.hero-or{left:387px;top:164px;color:var(--white);font-size:10.5px}

.info-form{left:477px;top:76px;width:170px;height:169px;background:var(--white);border:2px solid var(--brand-blue);border-radius:3px}
.info-form h2{position:absolute;top:7px;width:100%;text-align:center;color:var(--heading-blue);font-size:8px;font-weight:600}
.info-form p{position:absolute;top:22px;width:100%;text-align:center;color:var(--heading-blue);font-size:6.8px}
.field{position:absolute;left:19px;width:136px;height:17px;border-bottom:1px solid var(--brand-blue);box-shadow:0 1px 2px rgba(0,0,0,.12);font-size:6.8px;color:#888;padding:4px 8px}
.field.focused{border:1px solid var(--brand-blue)}
.btn-send{position:absolute;left:55px;top:140px;width:57px;height:17px;background:var(--brand-blue);color:var(--white);font-size:7.8px;font-weight:700;text-align:center;line-height:17px;border-radius:1px}

/* Intro */
.intro{left:234px;top:306px;width:400px;color:var(--ink-soft);font-weight:700;font-size:10px;line-height:12.5px}

/* Bands */
.bands{left:0;top:0}

.icon{width:36px;height:36px}
.sec-title{color:var(--heading-blue);font-weight:700;font-size:14.6px}
.sec-sub{font-size:8px;color:var(--ink)}
.body-copy{font-size:8.1px;line-height:10.5px;color:var(--ink)}
.read-more{font-size:6.8px;color:var(--heading-blue)}

/* Tech cards */
.tech-card{width:140px;height:65px;background:var(--white);box-shadow:0 1px 3px rgba(0,0,0,.12);padding:9px 8px 0}
.tech-card h3{font-size:6.9px;font-weight:600;color:var(--heading-blue);line-height:8px}
.tech-card p{font-size:5.9px;line-height:9px;margin-top:5px;color:var(--ink);height:27px}
.tech-card .read-more{font-size:5.9px;position:absolute;left:8px;bottom:6px}
.tech-card .ring{position:absolute;right:5px;bottom:4px;width:11px;height:11px;border:2px solid var(--brand-blue);border-radius:50%}

.comm-item{font-size:8px;line-height:12.5px;color:var(--ink);width:310px}
.comm-item b{font-weight:600}
.support-copy{font-size:7px;line-height:10.5px;width:410px;color:var(--ink)}
.support-copy b{font-weight:700}

.footer-rule{left:161px;top:1174px;width:502px;height:1px;background:var(--rule)}
.footer-text{left:0;top:1181px;width:834px;text-align:center;font-size:6px;color:var(--ink)}
</style>
</head>
<body>

<header class="abs site-header">
  <div class="abs brand"><span class="brand-mark"></span>harborline</div>
  <nav class="nav">
    <a style="left:343px">About Us</a>
    <a style="left:394px">Services</a>
    <a class="active" style="left:436px">Mobile Command</a>
    <a style="left:523px">Core Markets</a>
    <a style="left:587px">Blog</a>
    <a class="contact" style="left:621px">Contact Us</a>
  </nav>
</header>

<section>
  <div class="abs hero-photo" role="img" aria-label="Blurred photo of a crowded city street during a special event"></div>
  <h1 class="abs hero-title">OUR MOBILE COMMAND</h1>
  <div class="abs hero-sub">SPECIAL EVENTS SERVICES</div>
  <div class="abs btn-download"><strong>DOWNLOAD</strong><span>OUR BROCHURE</span></div>
  <div class="abs hero-or">OR</div>
  <form class="abs info-form">
    <h2>REQUEST MORE INFORMATION</h2>
    <p>Leve your contacts here and we will contact you</p>
    <div class="field focused" style="top:45px">Name</div>
    <div class="field" style="top:75px">Phone number</div>
    <div class="field" style="top:105px">E-mail address</div>
    <div class="btn-send">SEND</div>
  </form>
</section>

<p class="abs intro">TRUST HARBORLINE'S MOBILE COMMAND AND SPECIAL EVENT SERVICES TO KEEP YOUR NEXT SPECIAL EVENT SAFE, SECURE, AND “UNEVENTFUL.”</p>

<svg class="abs bands" width="834" height="1200" aria-hidden="true">
  <polygon points="0,346 663,346 834,584 161,584" fill="var(--band)"/>
  <polygon points="161,593 834,593 663,790 0,790" fill="var(--band)"/>
  <polygon points="0,798 663,798 834,1010 161,1010" fill="var(--band)"/>
  <polygon points="161,1020 834,1020 663,1156 0,1156" fill="var(--band)"/>
</svg>

<!-- Special events -->
<svg class="abs icon" style="left:161px;top:364px" viewBox="0 0 36 36" aria-hidden="true">
  <rect x="1" y="4" width="34" height="31" fill="none" stroke="#333" stroke-width="3"/>
  <rect x="1" y="4" width="34" height="6" fill="#333"/>
  <g fill="#333"><rect x="5" y="0" width="2" height="5"/><rect x="11" y="0" width="2" height="5"/><rect x="17" y="0" width="2" height="5"/><rect x="23" y="0" width="2" height="5"/><rect x="29" y="0" width="2" height="5"/></g>
  <rect x="7" y="14" width="22" height="16" fill="var(--brand-blue)"/>
  <polygon points="18,17 19.5,21 23,21 20,23 21,27 18,25 15,27 16,23 13,21 16.5,21" fill="#fff"/>
</svg>
<h2 class="abs sec-title" style="left:223px;top:360px">SPECIAL EVENTS</h2>
<div class="abs sec-sub" style="left:223px;top:381px">POSE SPECIAL CHALLENGES</div>
<p class="abs body-copy" style="left:235px;top:399px;width:422px">Managing security is stressful under the best of circumstances – planning for both the expected and unexpected is part of the job. But when you're tasked with securing a special event, emergency or disaster recovery, the “unexpected” takes on an additional dimension, pertaining not only to the security threats you may have to address but also to the uncertainty of security operations and technical infrastructure at your disposal.</p>
<div class="abs read-more" style="left:234px;top:448px">Read more</div>

<svg class="abs icon" style="left:161px;top:475px" viewBox="0 0 36 42" aria-hidden="true">
  <path d="M22 4a6 6 0 0 1 6 6M22 0a10 10 0 0 1 10 10" fill="none" stroke="var(--brand-blue)" stroke-width="1.5"/>
  <path d="M10 8l10 10-5 3-8-8z" fill="#333"/><rect x="12" y="18" width="3" height="6" fill="#333"/>
  <path d="M1 24h22v12H1z M23 27h7l5 5v4H23z" fill="#333"/>
  <rect x="4" y="27" width="16" height="3" fill="#fff"/><rect x="25" y="29" width="4" height="3" fill="#fff"/>
  <circle cx="8" cy="37" r="3" fill="#333" stroke="#fff" stroke-width="1"/><circle cx="28" cy="37" r="3" fill="#333" stroke="#fff" stroke-width="1"/>
</svg>
<h2 class="abs sec-title" style="left:223px;top:472px">HARBORLINE'S MOBILE COMMAND</h2>
<div class="abs sec-sub" style="left:223px;top:493px">SPECIAL EVENT SERVICES</div>
<p class="abs body-copy" style="left:234px;top:512px;width:424px">ServicesHarborline's Mobile Command and Special Event Services provides your special event with the same level of technology and resources you'd expect at a permanent installation. With a comprehensive, highly reliable and redundant set of surveillance, monitoring and communication systems at your disposal, our state-of-the-art mobile command center is equipped with everything you need to execute a successful event.</p>
<div class="abs read-more" style="left:234px;top:561px">Read more</div>

<!-- Security technologies -->
<svg class="abs icon" style="left:161px;top:610px;height:40px" viewBox="0 0 36 40" aria-hidden="true">
  <path d="M18 1L2 6v12c0 10 7 17 16 21 9-4 16-11 16-21V6z" fill="#333"/>
  <path d="M18 6L7 10v8c0 7 5 12 11 15 6-3 11-8 11-15v-8z" fill="var(--brand-blue)"/>
  <path d="M7 14c4-3 18-3 22 0" fill="none" stroke="#fff" stroke-width="1.5"/>
</svg>
<h2 class="abs sec-title" style="left:223px;top:606px">SECURITY TECHNOLOGIES</h2>

<div class="abs tech-card" style="left:234px;top:638px"><h3>RAPID VIDEO SYSTEM DEPLOYMENT</h3><p>Our cameras are designed to be deployed anywhere, even without power or Ethernet.</p><span class="read-more">Read more</span><span class="ring"></span></div>
<div class="abs tech-card" style="left:379px;top:638px"><h3>AERIAL DRONE SURVEILLANCE</h3><p>Equipped with high resolu-tion cameras and thermal imaging capabilities our drones provide a visual perspective</p><span class="read-more">Read more</span><span class="ring"></span></div>
<div class="abs tech-card" style="left:523px;top:638px"><h3>DRONE DETECTION TECHNOLOGY</h3><p>State-of-the-art drone detection technologies detect drone activity, pilot location and classify the drone's...</p><span class="read-more">Read more</span><span class="ring"></span></div>
<div class="abs tech-card" style="left:234px;top:707px"><h3>GUNFIRE DETECTION</h3><p>Our technology positively identifies gunfire, providing law enforcement and first responders with critical...</p><span class="read-more">Read more</span><span class="ring"></span></div>
<div class="abs tech-card" style="left:379px;top:707px"><h3>REAL-TIME WEATHER MONITORING</h3><p>Our mobile command vehicle has live reporting curated remotely by a dedicated meteorologist.</p><span class="read-more">Read more</span><span class="ring"></span></div>
<div class="abs tech-card" style="left:523px;top:707px"><h3>SOCIAL MEDIA MONITORING</h3><p>Equipped to monitor various social media platforms, we use real-time intel to detect threats based on key words...</p><span class="read-more">Read more</span><span class="ring"></span></div>

<!-- Communication systems -->
<svg class="abs icon" style="left:161px;top:816px" viewBox="0 0 36 34" aria-hidden="true">
  <path d="M8 8h26v18h-4v6l-6-6H8z" fill="var(--brand-blue)"/>
  <path d="M1 1h28v20H10l-6 5v-5H1z" fill="#333" stroke="#fff" stroke-width="1.5"/>
  <g fill="#fff"><circle cx="10" cy="11" r="1.5"/><circle cx="15" cy="11" r="1.5"/><circle cx="20" cy="11" r="1.5"/></g>
</svg>
<h2 class="abs sec-title" style="left:223px;top:812px">COMMUNICATION SYSTEMS</h2>

<svg class="abs" style="left:234px;top:853px" width="28" height="28" aria-hidden="true"><path d="M14 2a12 12 0 1 1-11 7M6 5a12 12 0 0 1 6-3" fill="none" stroke="var(--brand-blue)" stroke-width="2"/></svg>
<p class="abs comm-item" style="left:271px;top:853px;width:320px"><b>SYSTEMS LANDLINE TELEPHONE SERVICE –</b> Crisp, clear communications with landline handsets over cellular or satellite ensures intelligible audio.</p>

<svg class="abs" style="left:234px;top:899px" width="28" height="28" aria-hidden="true"><path d="M14 2a12 12 0 1 1-11 7M6 5a12 12 0 0 1 6-3" fill="none" stroke="var(--brand-blue)" stroke-width="2"/></svg>
<p class="abs comm-item" style="left:271px;top:899px;width:290px"><b>TWO-WAY RADIOS AND CELLULAR PTT RADOS</b> – Our two-way radios can be pro-grammed to our clients' operating frequencies...</p>
<div class="abs read-more" style="left:270px;top:929px;font-size:6.3px">Read more</div>

<svg class="abs" style="left:234px;top:956px" width="28" height="28" aria-hidden="true"><path d="M14 2a12 12 0 1 1-11 7M6 5a12 12 0 0 1 6-3" fill="none" stroke="var(--brand-blue)" stroke-width="2"/></svg>
<p class="abs comm-item" style="left:271px;top:956px;width:310px"><b>SATELLITE TV, RADIO, AND CELLULAR DATA</b> – Mobile command ensures continuous, high-speed, reliable data communications...</p>
<div class="abs read-more" style="left:270px;top:988px;font-size:6.3px">Read more</div>

<!-- Support services -->
<svg class="abs icon" style="left:161px;top:1037px" viewBox="0 0 36 36" aria-hidden="true">
  <path d="M26 6A15 15 0 1 0 18 33" fill="none" stroke="#333" stroke-width="4"/>
  <polygon points="22,1 32,6 23,12" fill="#333"/>
  <path d="M22 32a15 15 0 0 0 11-14" fill="none" stroke="var(--brand-blue)" stroke-width="2" stroke-dasharray="2 2"/>
</svg>
<h2 class="abs sec-title" style="left:224px;top:1033px">SUPPORT SERVICES</h2>
<p class="abs support-copy" style="left:233px;top:1067px"><b>PROFESSIONAL TECHNICAL STAFF</b> – Our highly knowledgeable technical staff ensures that the technology aboard the mobile command is expressly programmed and deployed for each event to maximize its effectiveness.</p>
<p class="abs support-copy" style="left:233px;top:1107px"><b>SEASONED SECURITY PROFESSIONALS</b> – Don't have a professional staff to plan and operate the security of your event? Harborline's professional staff holds decades of experience as first responders...</p>
<div class="abs read-more" style="left:234px;top:1134px;font-size:6.3px">Read more</div>

<footer>
  <div class="abs footer-rule"></div>
  <div class="abs footer-text">Privacy Policy &nbsp;&nbsp;|&nbsp;&nbsp; © 2020 Harborline Consulting. All Rights Reserved.</div>
</footer>

</body>
</html>
```